Eye catching business card

2 sided
Black background with logo in color on one side along with the words "Proudly serving the commercial and defense industries since 1975"
2nd side to contain contact information (see attached current business card) and "Waterjet, Composite, Precision Machining and Clean Room Manufacturing" with a very faint watermark of a waving USA Flag in the back ground.
Remove the "est. 195" from the current logo design

```html
<!DOCTYPE html>
<html lang="en">
<head>
<meta charset="utf-8">
<title>Northvale Fabrication Inc – Business Card</title>
<link href="https://fonts.googleapis.com/css2?family=Poppins:wght@300;400;500;600;700&display=swap" rel="stylesheet">
<style>
  :root {
    --stage: #a6a6a8;
    --card-black: #141416;
    --pattern-dark: #2a2a2d;
    --card-white: #f6f6f4;
    --brand-blue: #1f6fd1;
    --brand-blue-light: #2a9be0;
    --text-grey: #6b6d70;
    --text-dark: #3d3f42;
    --rule-grey: #9a9c9f;
    --flag-red: #efe0e1;
    --flag-blue: #dde3ec;
  }
  * { box-sizing: border-box; margin: 0; padding: 0; }
  html, body { width: 1200px; height: 960px; overflow: hidden; }
  body {
    background: var(--stage);
    font-family: "Poppins", sans-serif;
    position: relative;
  }
  .card {
    position: absolute;
    width: 700px;
    height: 400px;
    overflow: hidden;
    box-shadow: 0 10px 24px rgba(0,0,0,0.25);
  }

  /* Front: black side */
  .card-front { left: 60px; top: 60px; background: var(--card-black); }
  .card-front .pattern {
    position: absolute; inset: 0;
    background: radial-gradient(ellipse at 55% 40%, #3a3a3e 0%, var(--pattern-dark) 45%, var(--card-black) 100%);
  }
  .front-brand {
    position: absolute; left: 0; right: 0; top: 140px;
    display: flex; align-items: center; justify-content: center; gap: 16px;
  }
  .brand-square {
    width: 44px; height: 44px; background: var(--brand-blue); flex: none;
  }
  .front-brand .brand-name {
    font-weight: 600; font-size: 30px; letter-spacing: 1px;
    color: #8d8f93; text-transform: uppercase;
  }
  .front-rule {
    position: absolute; left: 190px; right: 190px; top: 208px;
    height: 1px; background: #5a5b5f;
  }
  .tagline {
    position: absolute; left: 0; right: 0; top: 300px;
    text-align: center; color: #ffffff; font-size: 17px; font-weight: 400;
  }

  /* Back: contact side */
  .card-back { left: 440px; top: 500px; background: var(--card-white); }
  .card-back .flag {
    position: absolute; inset: 0;
    background: linear-gradient(120deg, var(--flag-blue) 0%, var(--flag-blue) 28%, var(--flag-red) 62%, var(--card-white) 100%);
  }
  .back-brand {
    position: absolute; left: 40px; top: 62px;
    display: flex; align-items: center; gap: 12px;
  }
  .back-brand .brand-name {
    font-weight: 600; font-size: 19px; letter-spacing: 0.5px;
    color: var(--text-grey); text-transform: uppercase; white-space: nowrap;
  }
  .back-brand .brand-square { width: 34px; height: 34px; }
  .back-rule {
    position: absolute; left: 40px; width: 340px; top: 118px;
    height: 1px; background: var(--rule-grey);
  }
  .person {
    position: absolute; right: 40px; top: 40px; text-align: right;
  }
  .person-name {
    color: var(--brand-blue); font-weight: 600; font-size: 26px; letter-spacing: 0.5px;
    text-transform: uppercase; line-height: 1.1;
  }
  .person-title { color: var(--rule-grey); font-size: 17px; font-weight: 300; }
  .person-rule { height: 1px; background: var(--rule-grey); width: 220px; margin: 8px 0 10px auto; }
  .contact-list { list-style: none; font-size: 15px; color: var(--text-dark); line-height: 1.55; }
  .contact-list li { display: flex; justify-content: flex-end; align-items: center; gap: 8px; }
  .contact-list svg { width: 13px; height: 13px; fill: var(--brand-blue); }
  .address {
    position: absolute; left: 40px; top: 216px;
    font-size: 15px; color: var(--text-dark); line-height: 1.4;
  }
  .services { font-size: 19px; color: var(--text-grey); line-height: 1.25; margin-top: 2px; max-width: 420px; }
  .band-grey {
    position: absolute; left: 0; right: 0; bottom: 22px; height: 6px;
    background: var(--rule-grey);
    clip-path: polygon(0 0, 60% 0, 61% 100%, 0 100%);
  }
  .band-blue {
    position: absolute; left: 0; right: 0; bottom: 0; height: 46px;
    background: linear-gradient(90deg, var(--brand-blue), var(--brand-blue-light));
    clip-path: polygon(0 70%, 62% 70%, 66% 0, 100% 0, 100% 100%, 0 100%);
  }
  .website {
    position: absolute; right: 30px; bottom: 14px;
    color: #ffffff; font-size: 15px; font-weight: 400;
  }
</style>
</head>
<body>

<section class="card card-front">
  <div class="pattern" role="img" aria-label="Embossed repeating brand pattern on black"></div>
  <div class="front-brand">
    <span class="brand-square"></span>
    <span class="brand-name">Northvale Fabrication Inc</span>
  </div>
  <div class="front-rule"></div>
  <p class="tagline">Proudly serving the commercial &amp; defense industries since 1975</p>
</section>

<section class="card card-back">
  <div class="flag" role="img" aria-label="Very faint waving American flag watermark"></div>

  <div class="back-brand">
    <span class="brand-square"></span>
    <span class="brand-name">Northvale Fabrication Inc</span>
  </div>
  <div class="back-rule"></div>

  <div class="person">
    <p class="person-name">Dale Harmon</p>
    <p class="person-title">President</p>
    <div class="person-rule"></div>
    <ul class="contact-list">
      <li>555-014-0008
        <svg viewBox="0 0 16 16"><path d="M3 1l3 3-2 2c1 2 3 4 5 5l2-2 3 3-2 3C6 15 1 10 0 3z"/></svg>
      </li>
      <li>555-014-0040
        <svg viewBox="0 0 16 16"><rect x="4" y="1" width="8" height="5"/><rect x="1" y="6" width="14" height="7" rx="1"/><rect x="4" y="11" width="8" height="4" fill="#fff"/></svg>
      </li>
      <li>info@northvalefab.com
        <svg viewBox="0 0 16 16"><path d="M1 3h14v10H1z"/><path d="M1 3l7 6 7-6" fill="none" stroke="#fff" stroke-width="1.5"/></svg>
      </li>
    </ul>
  </div>

  <div class="address">
    <p>Northvale Fabrication, Inc.</p>
    <p>214 Ridgeline Rd., Millbrook, PA 17000</p>
    <p class="services">Waterjet, Composite, Precision Machining &amp;Clean Room Manufacturing</p>
  </div>

  <div class="band-grey"></div>
  <div class="band-blue"></div>
  <p class="website">www.northvalefab.com</p>
</section>

</body>
</html>
```